CustomerPath UX Overhaul - redesign to improve visitor journeys and conversions

I need my website brought to life, professional and engaging.
I can supply as much pictures as needed to create enhancing visuals. I need your team to review the website and create a list of ideas of what you need from me to bring this vision to life.
The company does 3d modeling, 3d printing with FDM and resin printers, CAD design, 3d scanning.
My website is https://qtforgeworks.com/
Please review it and give me your best.
Target Market(s)
cosplayer, filmmakers, life size prints, custom designs, redesign and scanning, large and small scale prints, replicating
Industry/Entity Type
CAD Design, Additive Manufacturing, 3D Printing, 3D Scanning
Coding
Coded - Design and coding required
Number of Pages Required
3 page
Requirements
Must have
- Professional and clean look, inviting, eye grabber

```html
<!DOCTYPE html>
<html lang="en">
<head>
<meta charset="utf-8">
<title>QT Forge Works – Custom 3D Printing &amp; Design</title>
<link href="https://fonts.googleapis.com/css2?family=Montserrat:wght@400;500;600;700&display=swap" rel="stylesheet">
<style>
:root{
  --navy:#1b1858;
  --navy-deep:#16134a;
  --band:#1f2a86;
  --ink:#111111;
  --text:#444444;
  --line:#bdbdbd;
  --light:#f4f4f4;
  --soft:#f0f0f0;
  --white:#ffffff;
  --accent:#3bb8f0;
  --photo-grey:#c4c5c8;
  --photo-wood:#7a5f3c;
  --photo-dark:#3a332b;
  --photo-copper:#b06a34;
  --photo-warm:#cdbf9f;
  --photo-slate:#5d6670;
  --photo-amber:#a7823f;
}
*{box-sizing:border-box;margin:0;padding:0}
html,body{width:1200px;height:3775px;overflow:hidden}
body{position:relative;font-family:'Montserrat',sans-serif;color:var(--ink);background:var(--white)}
.abs{position:absolute}
a{color:inherit;text-decoration:none}

/* header */
.site-nav{left:111px;top:0;width:977px;height:94px;background:var(--navy);border-radius:0 0 14px 14px;display:flex;align-items:center;padding:0 44px}
.brand{display:flex;align-items:center;gap:10px;color:var(--white);font-weight:600;font-size:17px}
.brand-mark{width:22px;height:22px;border-radius:50%;background:var(--accent)}
.nav-links{margin-left:auto;display:flex;gap:24px;color:var(--white);font-size:15px}
.nav-links .active{font-weight:700;text-decoration:underline;text-underline-offset:5px}

/* hero */
.hero{left:0;top:0;width:1200px;height:657px;background:var(--light)}
.hero-title{left:111px;top:212px;font-size:46px;line-height:53px;font-weight:700;color:var(--navy)}
.hero-copy{left:111px;top:340px;width:480px;font-size:16.5px;line-height:26px;color:var(--text)}
.btn{display:inline-flex;align-items:center;justify-content:center;background:var(--navy);color:var(--white);font-size:15px;font-weight:500;border-radius:5px}
.hero-btn{left:111px;top:435px;width:154px;height:37px}
.tile-grid{left:671px;top:157px;width:420px;height:382px;display:grid;grid-template-columns:repeat(3,1fr);gap:13px}
.tile{border-radius:9px;background:var(--photo-grey)}
.tile.dark{background:var(--photo-dark)}
.tile.wood{background:var(--photo-wood)}

/* featured */
.eyebrow{font-size:20px;font-weight:500;color:var(--navy)}
.section-title{font-size:37px;font-weight:600;color:var(--ink)}
.center{left:0;width:1200px;text-align:center}
.card{width:298px}
.card-img{height:226px;border-radius:8px}
.card-name{margin-top:18px;font-size:15.5px;font-weight:600;color:var(--navy)}
.card-price{margin-top:8px;font-size:16px;color:var(--ink)}
.card-link{margin-top:8px;display:inline-block;font-size:15.5px;text-decoration:underline;color:var(--ink)}
.round-btn{width:48px;height:48px;border-radius:50%;background:var(--navy);display:flex;align-items:center;justify-content:center}

/* about */
.about{left:0;top:1345px;width:1200px;height:643px;background:var(--soft)}
.photo{border-radius:8px}
.body-copy{font-size:15.5px;line-height:26px;color:var(--text)}
.sub-title{font-size:22px;font-weight:500;color:var(--navy)}

/* showcase */
.band{left:0;top:1988px;width:1200px;height:437px;background:var(--band)}
.show-img{left:114px;top:2202px;width:977px;height:445px;border-radius:12px;background:linear-gradient(180deg,#a88446,var(--photo-amber))}
.side-btn{width:66px;height:66px;border-radius:50%;background:var(--navy);border:6px solid var(--white);display:flex;align-items:center;justify-content:center}

/* contact */
.field{left:111px;width:493px;border:1.5px solid #9a9a9a;border-radius:6px;font-size:14.5px;color:#555;padding:12px 14px}
.info-head{font-size:15px;font-weight:600;color:var(--ink)}
.info-copy{font-size:15.5px;line-height:26px;color:var(--text)}

/* newsletter + footer */
.footer{left:0;top:3345px;width:1200px;height:430px;background:var(--navy-deep)}
.news-box{left:111px;top:3251px;width:977px;height:202px;background:var(--light);border-radius:12px;box-shadow:0 2px 10px rgba(0,0,0,.08)}
.footer-brand{left:0;width:1200px;top:3555px;display:flex;justify-content:center;align-items:center;gap:14px;color:var(--white);font-size:30px;font-weight:600}
.footer-brand .sq{width:30px;height:30px;background:var(--accent)}
.footer-links{left:0;width:1200px;top:3670px;display:flex;justify-content:center;gap:30px;color:var(--white);font-size:19px}
.footer-rule{left:111px;top:3714px;width:977px;height:1px;background:#6a6aa0}
.footer-small{top:3732px;font-size:13px;color:#c9c9e0}
</style>
</head>
<body>

<section class="abs hero" aria-label="Hero"></section>

<header class="abs site-nav">
  <div class="brand"><span class="brand-mark"></span>QT Forge Works</div>
  <nav class="nav-links">
    <a class="active">Home</a><a>About</a><a>Featured Products</a><a>Testimonials</a><a>Gallery</a><a>Contact Us</a>
  </nav>
</header>

<h1 class="abs hero-title">Custom 3D Printing &amp;<br>Design Solutions</h1>
<p class="abs hero-copy">We transform your creative ideas into tangible reality, building innovative designs and personalized solutions with precision 3D printing, layer by careful layer.</p>
<a class="abs btn hero-btn">Get Started &#8594;</a>

<div class="abs tile-grid" role="img" aria-label="Photo of a personalized dart holder stand with three flag-themed darts, split across nine rounded tiles">
  <div class="tile"></div><div class="tile"></div><div class="tile"></div>
  <div class="tile"></div><div class="tile dark"></div><div class="tile"></div>
  <div class="tile wood"></div><div class="tile dark"></div><div class="tile wood"></div>
</div>

<!-- Featured products -->
<p class="abs center eyebrow" style="top:742px">Featured Products</p>
<h2 class="abs center section-title" style="top:778px">Explore Trending Product Highlights</h2>

<article class="abs card" style="left:111px;top:860px">
  <div class="card-img" role="img" aria-label="Photo of a row of metallic bullet replica storage containers in copper, silver, red and gold" style="background:var(--photo-copper)"></div>
  <h3 class="card-name">Bullet Replica Storage Containers</h3>
  <p class="card-price">$45.95</p>
  <a class="card-link">Shop Now &#8594;</a>
</article>
<article class="abs card" style="left:450px;top:860px">
  <div class="card-img" role="img" aria-label="Photo of a personalized black and gold dart holder stand holding three darts" style="background:var(--photo-grey)"></div>
  <h3 class="card-name">Personalized Dart Holder Stand</h3>
  <p class="card-price">$14.95</p>
  <a class="card-link">Shop Now &#8594;</a>
</article>
<article class="abs card" style="left:788px;top:860px">
  <div class="card-img" role="img" aria-label="Photo of a softly glowing lithophane photo night light" style="background:var(--photo-warm)"></div>
  <h3 class="card-name">Custom 3D Lithophane Photo Night</h3>
  <p class="card-price">$19.95</p>
  <a class="card-link">Shop Now &#8594;</a>
</article>

<div class="abs round-btn" style="left:541px;top:1212px"><svg width="16" height="16" viewBox="0 0 16 16"><path d="M10 2 4 8l6 6" fill="none" stroke="#fff" stroke-width="2.2"/></svg></div>
<div class="abs round-btn" style="left:611px;top:1212px"><svg width="16" height="16" viewBox="0 0 16 16"><path d="M6 2l6 6-6 6" fill="none" stroke="#fff" stroke-width="2.2"/></svg></div>

<!-- About -->
<section class="abs about" aria-label="About"></section>
<div class="abs photo" role="img" aria-label="Photo of a copper bullet replica container standing on a wooden shelf" style="left:114px;top:1431px;width:185px;height:408px;background:var(--photo-copper)"></div>
<div class="abs photo" role="img" aria-label="Photo of a flag-painted hammer prop resting on a dark textured base" style="left:330px;top:1524px;width:219px;height:381px;background:var(--photo-slate)"></div>
<p class="abs sub-title" style="left:630px;top:1438px">About Us</p>
<h2 class="abs" style="left:630px;top:1474px;font-size:36px;line-height:44px;font-weight:600">Innovators in 3D<br>Printing Technology</h2>
<p class="abs body-copy" style="left:630px;top:1585px;width:470px">Lorem ipsum dolor sit amet, consectetur adipiscing elit, sed do eiusmod tempor incididunt ut labore et dolore magna aliqua. Quis ipsum suspendisse ultrices gravida.</p>
<div class="abs" style="left:630px;top:1682px;width:458px;height:1px;background:var(--line)"></div>
<p class="abs sub-title" style="left:630px;top:1704px">Our Mission</p>
<p class="abs body-copy" style="left:630px;top:1742px;width:475px">At QT Forge Works, our mission is to turn visions into reality, layer by layer. As a small family-owned business based in Connecticut, we are dedicated to providing high-quality 3D printing and engraving services for all kinds of projects.</p>
<a class="abs btn" style="left:630px;top:1866px;width:145px;height:37px">Read More &#8594;</a>

<!-- Showcase -->
<section class="abs band" aria-label="Gallery"></section>
<p class="abs center" style="top:2068px;font-size:20px;font-weight:500;color:var(--white)">Explore Our Creative Journey</p>
<h2 class="abs center" style="top:2104px;font-size:36px;font-weight:600;color:var(--white)">A Showcase Of 3d Printing And Design Projects</h2>
<div class="abs show-img" role="img" aria-label="Photo of a 3D printer nozzle close-up printing a red part inside a warm-lit enclosure"></div>
<div class="abs side-btn" style="left:75px;top:2389px"><svg width="18" height="18" viewBox="0 0 16 16"><path d="M10 2 4 8l6 6" fill="none" stroke="#fff" stroke-width="2.2"/></svg></div>
<div class="abs side-btn" style="left:1058px;top:2389px"><svg width="18" height="18" viewBox="0 0 16 16"><path d="M6 2l6 6-6 6" fill="none" stroke="#fff" stroke-width="2.2"/></svg></div>

<!-- Contact -->
<p class="abs sub-title" style="left:111px;top:2725px;font-size:20px">Contact Us</p>
<h2 class="abs" style="left:114px;top:2760px;font-size:37px;font-weight:600">Request A Free Consultation</h2>
<div class="abs field" style="top:2847px;height:42px">Name</div>
<div class="abs field" style="top:2906px;height:42px">Email Address</div>
<div class="abs field" style="top:2967px;height:82px">Message</div>
<div class="abs field" style="top:3066px;height:41px;display:flex;justify-content:space-between;align-items:center;padding-top:0;padding-bottom:0">Attach Files
  <svg width="14" height="16" viewBox="0 0 14 16"><path d="M10 5 5 10a1.8 1.8 0 0 0 2.5 2.5l5-5a3.5 3.5 0 0 0-5-5L2 8a5 5 0 0 0 7 7" fill="none" stroke="#444" stroke-width="1.3"/></svg>
</div>
<a class="abs btn" style="left:111px;top:3126px;width:144px;height:37px">Send &#8594;</a>

<p class="abs info-head" style="left:680px;top:2850px">We're Always Available To Talk Dreams!</p>
<p class="abs info-copy" style="left:680px;top:2876px;width:410px">We value our customers and are always ready to listen, collaborate, and create personalized products together.</p>
<p class="abs info-head" style="left:680px;top:2970px">QT Forge Works</p>
<p class="abs info-head" style="left:680px;top:2995px;font-size:14px;font-weight:500">Millbrook CT 06000</p>
<p class="abs info-copy" style="left:680px;top:3012px;font-size:14px">1 (860) 555.0142</p>
<p class="abs info-head" style="left:680px;top:3055px;font-size:14px">Hours</p>
<p class="abs info-copy" style="left:680px;top:3081px">Mon To Fri :09am - 05pm</p>

<!-- Newsletter + footer -->
<footer class="abs footer" aria-label="Footer"></footer>
<section class="abs news-box" aria-label="Newsletter"></section>
<h2 class="abs" style="left:174px;top:3298px;font-size:36px;line-height:44px;font-weight:600">Subscribe To<br>Our Newsletters</h2>
<div class="abs field" style="left:602px;top:3289px;width:424px;height:38px;padding:9px 24px">Email Address</div>
<a class="abs btn" style="left:602px;top:3343px;width:144px;height:37px">Subscribe &#8594;</a>
<p class="abs" style="left:605px;top:3399px;font-size:12px;color:var(--text)">Get 10% off your first purchase when you sign up for our newsletter!</p>

<div class="abs footer-brand"><span class="sq"></span>QT Forge Works</div>
<nav class="abs footer-links"><a>Home</a><a>About</a><a>Featured Products</a><a>Testimonials</a><a>Gallery</a><a>Contact Us</a></nav>
<div class="abs footer-rule"></div>
<p class="abs footer-small" style="left:111px">Copyright © 2025 QT Forge Works. All rights reserved.</p>
<p class="abs footer-small" style="right:112px">Socialbook &nbsp;&nbsp;|&nbsp;&nbsp; Snapgram</p>

</body>
</html>
```